Improved Business Card, Government Contracting

We are looking to update the design of our business cards. We would like to create a template that can be used for future employees and easy to update.

Halvorsen Advisory Partners, LLC is a Service Disabled Veteran Owned Small Business with headquarters located in Leavenworth, KS. Our current website is www.hapteam.com. We have contracts in KS and VA with expansion opportunities in various other states. Our primary line of work is within government contracting and providing consulting services to various organizations within the Bureau of Frontier Works. We would like to project a professional image of our company that is consistent with the industry. Provided are previous versions of our business card template that shows our logo as well. We would like to make sure the information on the cards are easily noticeable .

Target Market(s)

Government Officials
Fellow Small Business Contractors
Large Business Contractors (ex. TRUX, Keswell Barnaby, Pryde Okonjo Whitcombe)

Industry/Entity Type

Business

Contact Information for Business Card

Dale Fenwick
Office Manager
Halvorsen Advisory Partners
Ph: 913.555.0172
Email: d.fenwick@hapteam.us
www.hapteam.com

Requirements
Must have
• The business mailing address is:
• 31842 204th Lane
• Leavenworth, KS 66099
Nice to have
• Embossed lettering

```html
<!DOCTYPE html>
<html lang="en">
<head>
<meta charset="utf-8">
<title>Halvorsen Advisory Partners – Business Card</title>
<link rel="stylesheet" href="https://fonts.googleapis.com/css2?family=Arimo:wght@700&family=Roboto+Condensed:wght@400;700&display=swap">
<style>
  :root {
    --backdrop: #e9e7e4;
    --card: #ffffff;
    --brand-blue: #2f55a6;
    --fold-blue: #5f80c4;
    --accent-yellow: #f2e12a;
    --ink: #161616;
    --on-blue: #ffffff;
  }
  * { margin: 0; padding: 0; box-sizing: border-box; }
  html, body {
    width: 1200px; height: 952px; overflow: hidden;
    background: var(--backdrop);
  }
  .canvas { position: relative; width: 1200px; height: 952px; }

  .card {
    position: absolute;
    width: 560px; height: 320px;
    background: var(--card);
    box-shadow: 0 6px 18px rgba(0,0,0,0.18);
    overflow: hidden;
  }

  /* Front */
  .card--front { left: 70px; top: 110px; }
  .front-brand {
    position: absolute; inset: 0;
    display: flex; align-items: center; justify-content: center; gap: 18px;
  }
  .front-brand__mark { width: 34px; height: 34px; background: var(--brand-blue); flex: none; }
  .front-brand__name {
    font-family: "Arimo", Arial, sans-serif; font-weight: 700;
    font-size: 34px; line-height: 1.1; letter-spacing: 0.5px;
    color: var(--brand-blue); text-transform: uppercase;
  }

  /* Back */
  .card--back { left: 570px; top: 520px; }
  .back-panel { position: absolute; inset: 0; width: 560px; height: 320px; }
  .contact {
    position: absolute; right: 18px; top: 66px;
    font-family: "Roboto Condensed", "Arial Narrow", sans-serif;
    font-size: 14px; line-height: 20px; text-align: right;
    list-style: none; white-space: nowrap;
  }
  .contact__item { color: var(--on-blue); }
  .contact__item--link { color: var(--accent-yellow); }

  .holder { position: absolute; left: 30px; top: 190px; font-family: "Roboto Condensed", "Arial Narrow", sans-serif; }
  .holder__name { font-size: 20px; font-weight: 700; color: var(--brand-blue); line-height: 1.1; }
  .holder__title { font-size: 13px; color: var(--ink); }

  .company {
    position: absolute; left: 30px; bottom: 24px;
    display: flex; align-items: center; gap: 12px;
  }
  .company__mark { width: 22px; height: 22px; background: var(--brand-blue); flex: none; }
  .company__name {
    font-family: "Roboto Condensed", "Arial Narrow", sans-serif;
    font-weight: 700; font-size: 24px; color: var(--ink); white-space: nowrap;
  }
</style>
</head>
<body>
<main class="canvas">

  <section class="card card--front" aria-label="Card front">
    <div class="front-brand">
      <span class="front-brand__mark"></span>
      <span class="front-brand__name">Halvorsen<br>Advisory Partners</span>
    </div>
  </section>

  <section class="card card--back" aria-label="Card back">
    <svg class="back-panel" viewBox="0 0 560 320" aria-hidden="true">
      <polygon points="410,245 560,245 560,262 418,272" fill="var(--fold-blue)"/>
      <polygon points="340,0 560,0 560,245 395,245" fill="var(--brand-blue)"/>
    </svg>

    <ul class="contact">
      <li class="contact__item">913.555.0172</li>
      <li class="contact__item contact__item--link">www.hapteam.com</li>
      <li class="contact__item contact__item--link">d.fenwick@hapteam.us</li>
      <li class="contact__item">31842 204th Lane</li>
      <li class="contact__item">Leavenworth, KS 66099</li>
    </ul>

    <div class="holder">
      <p class="holder__name">Dale Fenwick</p>
      <p class="holder__title">Office Manager</p>
    </div>

    <div class="company">
      <span class="company__mark"></span>
      <span class="company__name">Halvorsen Advisory Partners, LLC</span>
    </div>
  </section>

</main>
</body>
</html>
```